Web design for cloud computing startup

Our company is called BrightLedgerHub and we are a cloud computing startup that automates the purchasing to payment process for any company. This is a B2B solution targeting small and medium enterprises across different industries. Our application allows buyers to create electronic purchase orders and send them to suppliers. In turn, suppliers can generate invoices based on purchase orders. In addition to organizing and formalizing interactions between buyers and suppliers our system is environment friendly as it significantly reduces the amount of paper buyers and suppliers use.

Our mission is to become the leader on the market of cloud based software for procurement by delivering easy-integrated and cost effective solutions to help our customers improve operational efficiency and boost profitability of business.

We need your help to design 2 pages:
- Homepage
- Content page

Please use 3 colors for the webpages: white, blue, and green. White and blue should be primary colors, while green should just emphasize that we are environment friendly solution.

The words we are using to describe the website are the following:
- Simple and minimalist
- Modern, clean and light
- Professional and reliable
- Creative (we want something different from standard website template)
- Calling to action

Please see attached design examples for homepage and content page that we like (please note that attached examples are only for the page structures not for the color schemes).

In addition to features mentioned in the attached ppt, homepage should have:
- Rotating banner with 3 different pictures (one of them featuring environmental aspect of our solution)
- Contact us on Pagewall, Quello, Tramvoy

Reason: I've updated the project brief, eliminating some of the requirements giving you more freedom.

Reason: Requests from designers to extend deadline

Target Market(s)

Small and Medium Enterprises. Primary users of the website are senior executives of those companies so website needs to account for this.

Industry/Entity Type

Environment

Requirements
Must have
• - For the final design we need PSD files with all the original layers
- The width needs to be a size that will work with every size computer screen
- Need to use cross-platform compatible font

Please feel free to ask any questions to help you refine your design.
Look forward to seeing your designs. Thank you all for your time and efforts.

```html
<!DOCTYPE html>
<html lang="en">
<head>
<meta charset="utf-8">
<title>Cloud Computing – BrightLedgerHub</title>
<link rel="stylesheet" href="https://fonts.googleapis.com/css2?family=Open+Sans:wght@400;600;700&family=Arimo:wght@700&display=swap">
<style>
:root{
  --blue:#0a5bb5;
  --blue-dark:#0a3f86;
  --blue-band:#0b4fa6;
  --blue-text:#0b63c1;
  --green:#6a9a1f;
  --green-band-top:#a8cf55;
  --green-band-bottom:#7fb02c;
  --grey-text:#555;
  --footer-bg:#f4f4f4;
  --bar:#6b6b6b;
  --white:#fff;
}
*{box-sizing:border-box;margin:0;padding:0}
html,body{width:1191px;height:1200px;overflow:hidden}
body{position:relative;background:var(--white);font-family:"Open Sans",Arial,sans-serif;color:var(--grey-text)}
a{color:inherit;text-decoration:none}

.site-header{position:absolute;left:0;top:0;width:1191px;height:93px;background:linear-gradient(#fff,#f6f7f8)}
.brand{position:absolute;left:126px;top:26px;font-size:35px;font-weight:400;color:var(--blue-text);letter-spacing:.5px}
.phone{position:absolute;left:893px;top:16px;display:flex;align-items:center;gap:6px;font-size:17px;font-weight:600;color:var(--blue-text);letter-spacing:.5px}
.search{position:absolute;left:887px;top:56px;width:177px;height:26px;border:1px solid #cfd3d6;background:#fff;font-size:15px;color:#666;padding:3px 8px}
.search svg{position:absolute;right:5px;top:4px}

.main-nav{position:absolute;left:0;top:93px;width:1191px;height:44px;background:linear-gradient(#fafafa,#e3e4e6);border-top:1px solid #e2e2e2}
.main-nav ul{list-style:none;display:flex;position:absolute;left:124px;top:0;height:44px;border-left:1px solid #d3d3d3}
.main-nav li{height:44px;line-height:42px;text-align:center;font-size:16px;color:#333;border-right:1px solid #d3d3d3}

.hero{position:absolute;left:0;top:137px;width:1191px;height:439px;background:linear-gradient(90deg,#0b3f95,#1466c4 50%,#0b3f95)}
.hero-panel{position:absolute;left:120px;top:14px;width:951px;height:393px;border:4px solid #fff;border-radius:8px;overflow:hidden}
.hero-visual{position:absolute;inset:0;background:radial-gradient(ellipse at 40% 25%,#e8f3fb 0%,#a9d3f1 30%,#4ea3e2 60%,#1a6fc2 100%)}
.hero-title{position:absolute;left:30px;top:30px;font-family:"Arimo",Arial,sans-serif;font-weight:700;font-size:37px;line-height:42px;color:var(--blue-dark);letter-spacing:1px}
.hero-copy{position:absolute;left:30px;top:130px;width:343px;font-size:15.5px;line-height:19.6px;color:#4a5866;text-align:justify;letter-spacing:.6px}
.btn-learn{position:absolute;left:21px;top:326px;width:128px;height:34px;border-radius:3px;background:var(--blue);color:#fff;font-size:17px;font-weight:600;line-height:34px;text-align:center}
.hero-dots{position:absolute;left:563px;top:415px;display:flex;gap:9px}
.hero-dots span{width:14px;height:14px;border-radius:50%;background:#fff}
.hero-dots .is-active{background:#6aa020;border:2px solid #fff}

.feature-band{position:absolute;left:0;top:576px;width:1191px;height:103px;background:linear-gradient(var(--green-band-top),var(--green-band-bottom))}
.feature{position:absolute;top:18px;display:flex;align-items:center;gap:14px}
.feature h3{font-size:25px;font-weight:400;color:#1c2b0c;line-height:30px}
.feature p{font-size:14px;color:#fff;margin-left:6px}

.content{position:absolute;left:0;top:679px;width:1191px;height:290px}
.col-title{position:absolute;top:23px;font-size:25px;font-weight:400}
.col-title .g{color:var(--green)}
.col-title .b{color:var(--blue-text)}
.video{position:absolute;left:128px;top:65px;width:258px;height:183px;background:linear-gradient(#ececec,#d8d8d8);border:1px solid #d0d0d0}
.divider{position:absolute;top:30px;width:8px;height:215px;background:radial-gradient(ellipse at left center,rgba(0,0,0,.12),transparent 70%)}
.why-copy{position:absolute;left:467px;top:62px;width:273px;font-size:13.6px;line-height:16.8px;color:#333;text-align:justify}
.btn-more{position:absolute;left:637px;top:224px;width:103px;height:26px;border-radius:3px;background:linear-gradient(#3ba0ef,#0e72cf);color:#fff;font-size:13px;font-weight:600;line-height:26px;padding-left:8px}
.btn-more svg{position:absolute;right:0;top:0}
.login label{position:absolute;left:814px;font-size:16px;color:#444}
.login .field{position:absolute;left:913px;width:145px;height:27px;border:1px solid #c8c8c8;border-radius:5px;background:linear-gradient(#e6e6e6,#f7f7f7)}
.btn-login{position:absolute;left:977px;top:168px;width:80px;height:29px;border-radius:4px;background:linear-gradient(#3aa0ef,#0d70cf);color:#fff;font-size:16px;font-weight:600;line-height:29px;text-align:center}
.login-links{position:absolute;right:131px;top:210px;font-size:14px;color:var(--green)}

.site-footer{position:absolute;left:0;top:969px;width:1191px;height:201px;background:linear-gradient(#efefef,#fafafa);border-top:2px solid #e2e2e2}
.footer-col{position:absolute;top:18px}
.footer-col h4{font-size:16px;font-weight:400;color:var(--blue-text);margin-bottom:10px}
.footer-col li{list-style:none;font-size:13.6px;line-height:23.3px;color:#444;display:flex;align-items:center;gap:6px}
.social-dot{width:17px;height:17px;border-radius:2px;background:var(--blue)}
.copyright{position:absolute;left:0;top:1170px;width:1191px;height:30px;background:var(--bar);color:#fff;font-size:13.6px;line-height:30px;text-align:right;padding-right:126px;letter-spacing:.4px}
</style>
</head>
<body>

<header class="site-header">
  <div class="brand">Cloud Computing</div>
  <div class="phone">
    <svg width="26" height="30" viewBox="0 0 26 30"><path d="M5 2c2-1 4 0 5 2l2 4c1 2 0 3-1 4l-2 1c1 4 4 8 8 10l2-2c1-1 3-1 4 0l2 3c1 2 0 4-2 5-4 2-9-1-13-6S1 8 2 5c0-1 1-2 3-3z" fill="#1a74d0"/></svg>
    <span>1800-555-0147</span>
  </div>
  <div class="search">Search
    <svg width="18" height="18" viewBox="0 0 18 18"><circle cx="7" cy="7" r="5" fill="none" stroke="#666" stroke-width="2"/><path d="M11 11l5 5" stroke="#666" stroke-width="3" stroke-linecap="round"/></svg>
  </div>
</header>

<nav class="main-nav">
  <ul>
    <li style="width:93px">Home</li>
    <li style="width:123px">Company</li>
    <li style="width:121px">Solutions</li>
    <li style="width:141px">How to save</li>
    <li style="width:155px">Save the Earth</li>
    <li style="width:185px">Knowledge center</li>
    <li style="width:124px">Contact us</li>
  </ul>
</nav>

<section class="hero">
  <div class="hero-panel">
    <div class="hero-visual" role="img" aria-label="Banner scene: bright sky with clouds over a reflective surface and a large glass cloud shape on the right"></div>
    <h1 class="hero-title">We build applications<br>for the cloud.</h1>
    <p class="hero-copy">Lorem ipsum dolor sit amet, consectetur adipiscing elit. Morbi mollis lorem quis diam euismod in fermentum mauris consectetur. Class aptent taciti sociosqu ad litora torquent per conubia nostra, per inceptos himenaeos. Proin a gravida nisl. In eleifend augue turpis, sit amet iaculis nunc.</p>
    <a class="btn-learn" href="#">Learn More</a>
  </div>
  <div class="hero-dots"><span class="is-active"></span><span></span><span></span></div>
</section>

<section class="feature-band">
  <div class="feature" style="left:137px">
    <svg width="92" height="68" viewBox="0 0 92 68"><path d="M4 22C4 10 16 4 28 4s24 6 24 18-12 18-24 18c-4 0-7 0-10-2l-10 6 3-9C6 32 4 27 4 22z" fill="#1b74c9"/><path d="M32 34c0-12 12-18 26-18s28 6 28 18-12 18-26 18c-4 0-8 0-11-2l-2 14-6-17c-6-3-9-8-9-13z" fill="#4aa6e6"/></svg>
    <div><h3>Testimonials</h3><p>Lorem ipsum dolor sit</p></div>
  </div>
  <div class="feature" style="left:486px">
    <svg width="72" height="72" viewBox="0 0 72 72"><circle cx="36" cy="36" r="33" fill="#6cb41f"/><circle cx="36" cy="36" r="28" fill="#83cc2c"/><text x="36" y="50" text-anchor="middle" font-family="Open Sans,Arial,sans-serif" font-weight="700" font-size="40" fill="#fff">$</text></svg>
    <div><h3>Pricing</h3><p>Lorem ipsum dolor sit</p></div>
  </div>
  <div class="feature" style="left:808px">
    <svg width="68" height="72" viewBox="0 0 68 72"><circle cx="34" cy="34" r="32" fill="#e8eef2"/><circle cx="34" cy="34" r="26" fill="#1d8ad2"/><text x="34" y="48" text-anchor="middle" font-family="Open Sans,Arial,sans-serif" font-weight="700" font-size="38" fill="#fff">?</text></svg>
    <div><h3>FAQ’s</h3><p>Lorem ipsum dolor sit</p></div>
  </div>
</section>

<main class="content">
  <h2 class="col-title" style="left:126px"><span class="g">BLH</span> <span class="b">video</span></h2>
  <div class="video">
    <svg width="258" height="183" viewBox="0 0 258 183"><circle cx="130" cy="93" r="33" fill="#c4c4c4"/><path d="M120 75l28 18-28 18z" fill="#fff"/></svg>
  </div>

  <div class="divider" style="left:428px"></div>
  <h2 class="col-title" style="left:465px"><span class="g">Why</span> <span class="b">BLH</span></h2>
  <p class="why-copy">Lorem ipsum dolor sit amet, consectetur adipiscing elit. Duis sed velit eros, et volutpat dui. Aliquam erat volutpat. Donec dictum interdum gravida. Integer enim massa, tincidunt quis vulputate eu, tincidunt nec lectus. Curabitur eget dolor eget eros semper facilisis volutpat eu diam. Maecenas sed ultricies arcu. lum ligula egestas sit amet.</p>
  <a class="btn-more" href="#">Read More
    <svg width="20" height="26" viewBox="0 0 20 26"><path d="M0.5 0v26" stroke="#8cc6f5"/><path d="M8 10l5 3-5 3z" fill="#fff"/></svg>
  </a>

  <div class="divider" style="left:779px"></div>
  <h2 class="col-title" style="left:811px"><span class="g">Client</span> <span class="b">Login</span></h2>
  <form class="login">
    <label style="top:86px">User Name</label>
    <span class="field" style="top:83px"></span>
    <label style="top:132px">Password</label>
    <span class="field" style="top:128px"></span>
    <span class="btn-login">Login</span>
    <span class="login-links">Forgot your password | Register</span>
  </form>
</main>

<footer class="site-footer">
  <div class="footer-col" style="left:128px"><h4>Company</h4><ul><li>About BLH</li><li>Why BLH</li><li>Customer testimonials</li><li>Our management</li><li>Careers</li></ul></div>
  <div class="footer-col" style="left:335px"><h4>Solutions</h4><ul><li>Procure-to pay process</li><li>For suppliers</li><li>For buyers</li><li>Pricing</li><li>Application integration</li><li>Privacy policy</li></ul></div>
  <div class="footer-col" style="left:533px"><h4>How to save</h4><ul><li>Speed up your processes</li><li>Simplify your procedures</li><li>Savings calculators</li></ul></div>
  <div class="footer-col" style="left:733px"><h4>Knowledge center</h4><ul><li>Industry news</li><li>White papers</li><li>Trainings/Webinars</li><li>Success stories</li><li>FAQ’s</li></ul></div>
  <div class="footer-col" style="left:928px"><h4>Connect With Us</h4><ul><li><span class="social-dot"></span>Pagewall</li><li><span class="social-dot"></span>Quello</li><li><span class="social-dot"></span>Tramvoy</li></ul></div>
</footer>
<div class="copyright">©Copyright 2011 Cloud Computing.</div>

</body>
</html>
```